tri fold logistics company FLYER and A4 COMPANY FLYER COVER and A4 company flyer

we need to design company tri fold brochure and A4 company flyer cover for us
our company website is www.halvornfreight.com
pls design for us asap

ALSO OUR COMPANY NAME IS HALVORN FREIGHT INC
NOT " HALVORN FREIGHT, INC"

CAN YOU DESIGN THE COMPANY EMAIL SIGNATURE FOR US TOO

Target Market(s)

customer in U.S.

Industry/Entity Type

Freight Forwarding

Requirements
Must have
• company name and logo
• company name; HALVORN FREIGHT INC
Nice to have
• international shipping map,

```html
<!DOCTYPE html>
<html lang="en">
<head>
<meta charset="utf-8">
<title>Halvorn Freight Inc — Tri-fold Brochure</title>
<link href="https://fonts.googleapis.com/css2?family=Cinzel:wght@500;600&family=Open+Sans:ital,wght@0,400;0,600;0,700;1,400&display=swap" rel="stylesheet">
<style>
:root{
  --navy:#1d3768;
  --navy-deep:#14284f;
  --blue:#2f4f8c;
  --blue-soft:#4a6aa8;
  --sky:#c9d6e8;
  --mist:#eef1f6;
  --paper:#ffffff;
  --ink:#2b3550;
  --ink-soft:#5a6480;
  --backdrop:#e6e6e6;
}
*{box-sizing:border-box;margin:0;padding:0}
html,body{width:1200px;height:2400px;overflow:hidden}
body{background:var(--backdrop);font-family:"Open Sans",Arial,sans-serif;color:var(--ink);position:relative}
.spread{position:absolute;left:40px;width:1120px;height:866px;display:flex;box-shadow:0 12px 30px rgba(0,0,0,.18)}
.spread--outside{top:222px}
.spread--inside{top:1310px}
.panel{position:relative;width:373.33px;height:100%;overflow:hidden;background:var(--paper)}
.panel + .panel{border-left:1px solid rgba(0,0,0,.06)}

/* shared pieces */
.photo{position:absolute}
.photo--circle{border-radius:50%;border:6px solid rgba(255,255,255,.85)}
.ribbon{position:absolute;left:0;right:0;height:30px;background:linear-gradient(90deg,var(--navy-deep),var(--blue));color:#fff;font-size:11px;font-weight:700;letter-spacing:.08em;display:flex;align-items:center;padding-left:26px;line-height:1.2}
.copy{position:absolute;left:26px;right:26px;font-size:9.5px;line-height:1.55;color:var(--ink-soft)}
.copy p + p{margin-top:7px}
.bullets{list-style:none;margin-top:8px}
.bullets li{position:relative;padding-left:13px;margin-bottom:3px;color:var(--ink)}
.bullets li::before{content:"";position:absolute;left:0;top:4px;width:6px;height:6px;border-radius:50%;background:var(--blue)}
.brand{display:flex;align-items:center;gap:10px;font-family:"Cinzel",Georgia,serif;font-weight:600;letter-spacing:.04em;white-space:nowrap}
.brand__mark{width:30px;height:30px;border-radius:50%;border:2px solid currentColor;flex:none}
.web{font-size:14px;letter-spacing:.06em;color:#fff}
.curve{position:absolute;left:0;width:100%}

/* outside: flap */
.flap{background:var(--mist)}
.flap .ribbon--one{top:52px;padding-right:120px}
.flap .ribbon--two{top:392px;padding-left:124px}
.flap .photo--one{top:22px;right:18px;width:92px;height:92px;background:radial-gradient(circle at 40% 40%,#d98a6a,#7a4a3a 55%,#35425e)}
.flap .photo--two{top:362px;left:18px;width:92px;height:92px;background:radial-gradient(circle at 50% 40%,#c7a27a,#6f5840 55%,#3a3a48)}
.flap .copy--one{top:124px}
.flap .copy--two{top:466px}
.flap__band{bottom:0;height:150px}
.flap__note{position:absolute;left:30px;right:30px;bottom:34px;color:#dfe6f3;font-size:9px;font-style:italic;line-height:1.5}

/* outside: back panel */
.about .brand{position:absolute;top:46px;left:0;right:0;justify-content:center;color:var(--navy);font-size:19px}
.about__pill{position:absolute;top:104px;left:70px;right:70px;height:26px;border-radius:13px;background:linear-gradient(90deg,var(--navy-deep),var(--blue-soft));color:#fff;font-size:11px;font-weight:700;letter-spacing:.1em;display:flex;align-items:center;justify-content:center}
.about .copy{top:146px}
.about__badge{position:absolute;top:470px;left:30px;width:84px;height:30px;border-radius:4px;background:linear-gradient(90deg,#1f3a6e,#3c8fc2)}
.about__badge-note{position:absolute;top:478px;left:126px;right:26px;font-size:9px;color:var(--ink-soft)}
.about__band{bottom:0;height:310px}
.contact{position:absolute;bottom:92px;left:0;right:0;text-align:center;color:#e6ecf7;font-size:11px;line-height:1.6;font-style:italic}
.about .web{position:absolute;bottom:36px;left:0;right:0;text-align:center}

/* outside: cover */
.cover{background:var(--navy)}
.cover__scene{top:0;left:0;width:100%;height:480px;background:linear-gradient(180deg,#1d3768 0%,#6f88b2 30%,#d8e1ee 62%,#a9b7cc 100%)}
.cover .brand{position:absolute;top:58px;left:0;right:0;justify-content:center;color:#fff;font-size:19px}
.cover__band{top:420px;height:446px}
.cover__people{top:450px;left:101px;width:172px;height:172px;background:radial-gradient(circle at 50% 35%,#e9eef6,#9aa9c2 55%,#2a3550)}
.cover__tagline{position:absolute;top:660px;left:20px;right:20px;text-align:center;color:#fff;font-size:16px;line-height:1.45;letter-spacing:.04em}
.cover__webbar{position:absolute;bottom:40px;left:0;right:0;height:40px;background:linear-gradient(90deg,rgba(255,255,255,0),rgba(255,255,255,.16),rgba(255,255,255,0));display:flex;align-items:center;justify-content:center}

/* inside: express panel */
.express{background:var(--navy)}
.express__scene{top:0;left:0;width:100%;height:460px;background:linear-gradient(180deg,#8ea4c6 0%,#dfe6ef 35%,#b2554a 60%,#2b4f86 80%,#1d3768 100%)}
.express__band{top:400px;height:466px}
.express__mark{position:absolute;top:420px;left:131px;width:112px;height:112px;border-radius:50%;background:var(--mist);border:6px solid rgba(255,255,255,.6);display:flex;align-items:center;justify-content:center;text-align:center;font-family:"Cinzel",Georgia,serif;font-weight:600;font-size:11px;line-height:1.25;color:var(--navy)}
.express__lead{position:absolute;top:556px;left:26px;right:26px;text-align:center;color:#fff;font-size:14.5px;line-height:1.4}
.express .copy{top:640px;color:#dbe3f1}

/* inside: rates panel */
.rates{background:var(--blue)}
.rates__map{top:0;left:0;width:100%;height:150px;background:linear-gradient(160deg,#e9eef5,#bccbe0 60%,#9fb3d2)}
.rate-table{position:absolute;left:18px;width:calc(100% - 36px);background:#fff;font-size:9.5px;border-collapse:collapse}
.rate-table caption{caption-side:top;text-align:left;background:var(--navy-deep);color:#fff;font-weight:700;font-size:10px;letter-spacing:.06em;padding:5px 8px}
.rate-table th{background:var(--sky);color:var(--navy);text-align:left;padding:3px 8px;font-weight:700}
.rate-table td{padding:3px 8px;border-bottom:1px solid #dde3ee;color:var(--ink)}
.rate-table td:not(:first-child),.rate-table th:not(:first-child){text-align:right}
.rate-table--one{top:170px}
.rate-table--two{top:400px}
.rate-table--three{top:630px}

/* inside: services panel */
.services .ribbon--one{top:52px;padding-right:120px}
.services .ribbon--two{top:470px;padding-left:124px;padding-right:12px;height:34px}
.services .photo--one{top:22px;right:18px;width:92px;height:92px;background:radial-gradient(circle at 50% 45%,#c8d3e3,#5b6f93 55%,#24375e)}
.services .photo--two{top:440px;left:18px;width:92px;height:92px;background:radial-gradient(circle at 50% 40%,#e4e9f0,#7d8ba4 55%,#2e3a54)}
.services .copy--one{top:126px}
.services .copy--two{top:548px}
.partner{position:absolute;right:26px;bottom:26px;font-size:15px;font-weight:700;color:var(--blue)}
</style>
</head>
<body>

<section class="spread spread--outside">

  <article class="panel flap">
    <div class="photo photo--circle photo--one" role="img" aria-label="Photo of a delivery truck on a highway"></div>
    <h2 class="ribbon ribbon--one">DOMESTIC SHIPPING</h2>
    <div class="copy copy--one">
      <p>Halvorn Freight offers full truckload and less-than-truckload service to every state. Our dispatch team tracks each load from pickup to delivery and keeps you informed along the way.</p>
      <p>We partner with vetted carriers to move your cargo safely, quickly and at a fair cost, whether you ship one pallet or a full trailer.</p>
      <ul class="bullets">
        <li>Full truckload (FTL)</li>
        <li>Less than truckload (LTL)</li>
        <li>Intermodal rail service</li>
        <li>Residential and liftgate delivery</li>
        <li>Warehouse and cross-dock</li>
      </ul>
    </div>
    <div class="photo photo--circle photo--two" role="img" aria-label="Photo of warehouse workers loading parcels"></div>
    <h2 class="ribbon ribbon--two">FBA FORWARDING SERVICES</h2>
    <div class="copy copy--two">
      <p>We prepare, label and deliver your goods to fulfillment centers across the country, meeting every appointment and packing rule.</p>
      <ul class="bullets">
        <li>Carton and pallet labeling</li>
        <li>Inspection and repacking</li>
        <li>Appointment booking</li>
        <li>Short-term storage</li>
      </ul>
    </div>
    <svg class="curve flap__band" viewBox="0 0 373 150" preserveAspectRatio="none" aria-hidden="true">
      <path d="M0 40 Q190 0 373 30 L373 150 L0 150 Z" fill="#1d3768"/>
    </svg>
    <p class="flap__note">Every shipment is handled with care by a team that treats your freight as if it were our own.</p>
  </article>

  <article class="panel about">
    <div class="brand"><span class="brand__mark"></span>HALVORN FREIGHT INC</div>
    <h2 class="about__pill">ABOUT US</h2>
    <div class="copy">
      <p>Halvorn Freight Inc is a licensed freight forwarder serving importers and exporters across the U.S. We combine ocean, air and ground service to give our clients one trusted partner for every move.</p>
      <p>Our team brings years of trade know-how and close ties with carriers around the world, so your cargo moves on time and on budget.</p>
      <ul class="bullets">
        <li>Ocean freight, FCL and LCL</li>
        <li>Air freight and expedited cargo</li>
        <li>Customs clearance support</li>
        <li>Domestic trucking</li>
        <li>Cargo insurance</li>
        <li>Door-to-door service</li>
      </ul>
    </div>
    <div class="about__badge" role="img" aria-label="Partner network badge"></div>
    <p class="about__badge-note">Member of a global forwarder network.</p>
    <svg class="curve about__band" viewBox="0 0 373 310" preserveAspectRatio="none" aria-hidden="true">
      <path d="M0 120 Q190 40 373 90 L373 310 L0 310 Z" fill="#1d3768"/>
      <path d="M0 120 Q190 40 373 90" fill="none" stroke="#4a6aa8" stroke-width="3"/>
    </svg>
    <div class="contact">
      Our friendly staff is available 24 hours a day,<br>
      7 days a week. Feel free to contact us.<br>
      Phone: 1-555-014-2270<br>
      Fax: 1-555-014-2271<br>
      info@halvornfreight.com
    </div>
    <p class="web">www.halvornfreight.com</p>
  </article>

  <article class="panel cover">
    <div class="photo cover__scene" role="img" aria-label="Photo of port cranes, a container ship and a plane in the sky"></div>
    <div class="brand"><span class="brand__mark"></span>HALVORN FREIGHT INC</div>
    <svg class="curve cover__band" viewBox="0 0 373 446" preserveAspectRatio="none" aria-hidden="true">
      <path d="M0 70 Q190 0 373 40 L373 446 L0 446 Z" fill="#1d3768"/>
    </svg>
    <div class="photo photo--circle cover__people" role="img" aria-label="Photo of a business team looking upward"></div>
    <p class="cover__tagline">HALVORN FREIGHT, YOUR SOLUTION<br>TO ALL YOUR SHIPPING NEEDS!</p>
    <div class="cover__webbar"><span class="web">www.halvornfreight.com</span></div>
  </article>

</section>

<section class="spread spread--inside">

  <article class="panel express">
    <div class="photo express__scene" role="img" aria-label="Photo of a container ship at sea"></div>
    <svg class="curve express__band" viewBox="0 0 373 466" preserveAspectRatio="none" aria-hidden="true">
      <path d="M0 60 Q190 0 373 50 L373 466 L0 466 Z" fill="#1d3768"/>
    </svg>
    <div class="express__mark">HALVORN<br>FREIGHT</div>
    <p class="express__lead">When your shipment is too big to fly but also pressing enough that time is a significant factor, this service is for you.</p>
    <div class="copy">
      <p>We offer expedited ocean service from Shanghai, Ningbo and Xiamen to the U.S. West Coast. Priority loading and fast unloading cut days off the usual transit time.</p>
      <p>From the port we connect to rail and truck service that reaches major cities in the Midwest and on the East Coast.</p>
    </div>
  </article>

  <article class="panel rates">
    <div class="photo rates__map" role="img" aria-label="Map of ocean routes from China to the U.S. West Coast"></div>
    <table class="rate-table rate-table--one">
      <caption>FROM SHANGHAI</caption>
      <tr><th>Destination</th><th>Via</th><th>Transit</th></tr>
      <tr><td>Los Angeles</td><td>Port</td><td>11 days</td></tr>
      <tr><td>Long Beach</td><td>Port</td><td>11 days</td></tr>
      <tr><td>Oakland</td><td>Port</td><td>13 days</td></tr>
      <tr><td>Chicago</td><td>Rail</td><td>16 days</td></tr>
      <tr><td>Dallas</td><td>Rail</td><td>17 days</td></tr>
      <tr><td>New York</td><td>Rail</td><td>19 days</td></tr>
    </table>
    <table class="rate-table rate-table--two">
      <caption>FROM NINGBO</caption>
      <tr><th>Destination</th><th>Via</th><th>Transit</th></tr>
      <tr><td>Los Angeles</td><td>Port</td><td>12 days</td></tr>
      <tr><td>Long Beach</td><td>Port</td><td>12 days</td></tr>
      <tr><td>Oakland</td><td>Port</td><td>14 days</td></tr>
      <tr><td>Chicago</td><td>Rail</td><td>17 days</td></tr>
      <tr><td>Dallas</td><td>Rail</td><td>18 days</td></tr>
      <tr><td>New York</td><td>Rail</td><td>20 days</td></tr>
    </table>
    <table class="rate-table rate-table--three">
      <caption>FROM XIAMEN</caption>
      <tr><th>Destination</th><th>Via</th><th>Transit</th></tr>
      <tr><td>Los Angeles</td><td>Port</td><td>13 days</td></tr>
      <tr><td>Long Beach</td><td>Port</td><td>13 days</td></tr>
      <tr><td>Oakland</td><td>Port</td><td>15 days</td></tr>
      <tr><td>Chicago</td><td>Rail</td><td>18 days</td></tr>
      <tr><td>Dallas</td><td>Rail</td><td>19 days</td></tr>
    </table>
  </article>

  <article class="panel services">
    <div class="photo photo--circle photo--one" role="img" aria-label="Photo of a container vessel in port"></div>
    <h2 class="ribbon ribbon--one">OCEAN FREIGHT SERVICES</h2>
    <div class="copy copy--one">
      <p>We handle full container and consolidated loads on all major trade lanes. Our team books space, prepares documents and tracks each box until it reaches your door.</p>
      <p>With contracts on many carriers we find the best route and rate for every shipment, large or small.</p>
      <ul class="bullets">
        <li>FCL and LCL service</li>
        <li>Port-to-port or door-to-door</li>
        <li>Reefer and oversized cargo</li>
        <li>Bonded warehouse links</li>
        <li>Online cargo tracking</li>
      </ul>
    </div>
    <div class="photo photo--circle photo--two" role="img" aria-label="Photo of cargo being loaded onto an aircraft"></div>
    <h2 class="ribbon ribbon--two">AIR SHIPMENTS AND EXPEDITED DELIVERY</h2>
    <div class="copy copy--two">
      <p>When speed matters most, our air desk moves your cargo on direct and consolidated flights worldwide, with pickup and delivery at both ends.</p>
      <p>Next-flight-out, charter and time-definite options keep urgent goods on schedule, with live updates from our staff.</p>
    </div>
    <p class="partner">Corvane Lines</p>
  </article>

</section>

</body>
</html>
```